Business Card Design

This is a new business to be run from my home. I have attended certificate workshops run by Dr Kevin Ruddock who is a Master Trainer in Gentle Flow for Mobility.
I wish to communicate to people that Tai Chi is for everyone, no matter their age, gender or fitness levels. Tai Chi is taught both standing & seated.
The card should have a slightly Asian feel, mainly printed in black & white with perhaps a little soft pink &/or green.

Target Market(s)

people of all ages from 10 years up, poor fitness & mild disabilities.

Industry/Entity Type

Fitness

Contact Information for Business Card

Marrowdene Flowing Arts for Body, Mind & Stillness

Brenna Holcroft, Certificated Leader

ph 5281 9046

Requirements
Nice to have
• a feeling of health & peace.
Should not have
• bright colours, fancy fonts

```html
<!DOCTYPE html>
<html lang="en">
<head>
<meta charset="utf-8">
<title>Tai Chi For All – Business Card</title>
<link rel="stylesheet" href="https://fonts.googleapis.com/css2?family=Cinzel:wght@400;500&family=Gentium+Book+Plus&family=Questrial&display=swap">
<style>
  :root {
    --paper: #ffffff;
    --scene-light: #f4f4f4;
    --scene-mid: #e2e2e2;
    --scene-dark: #cfcfcf;
    --figure-tone: rgba(250, 250, 250, 0.55);
    --title-green: #3bee35;
    --title-edge: #1b7d1b;
    --title-glow: #b9f7b5;
    --soft-green: #6fbf6c;
    --tag-green: #5cc45a;
    --ink: #111111;
  }
  * { margin: 0; padding: 0; box-sizing: border-box; }
  html, body { width: 1200px; height: 900px; overflow: hidden; background: var(--paper); }
  .card { position: relative; width: 1200px; height: 900px; background: var(--paper); overflow: hidden; }

  .scene-backdrop {
    position: absolute; left: 0; top: 100px; width: 1200px; height: 800px;
    background:
      radial-gradient(ellipse 420px 300px at 330px 360px, var(--scene-mid), transparent 70%),
      linear-gradient(180deg, var(--scene-light) 0%, var(--scene-light) 52%, var(--scene-mid) 68%, var(--scene-dark) 100%);
  }
  .figure-art {
    position: absolute; left: 625px; top: 112px; width: 530px; height: 700px;
    background: linear-gradient(180deg, var(--figure-tone), rgba(250,250,250,0.25));
    border-radius: 220px 200px 60px 60px;
  }

  .title {
    position: absolute; left: 40px; top: 262px;
    font-family: "Cinzel", "Times New Roman", serif; font-weight: 500;
    font-size: 186px; line-height: 1; letter-spacing: 2px;
    color: var(--title-green);
    -webkit-text-stroke: 2px var(--title-edge);
    text-shadow: 0 0 4px var(--title-glow), 0 0 8px var(--title-glow);
  }
  .subtitle {
    position: absolute; left: 936px; top: 376px;
    font-family: "Cinzel", "Times New Roman", serif; font-weight: 400;
    font-size: 52px; line-height: 1; color: var(--soft-green);
  }
  .tagline {
    position: absolute; right: 28px; top: 458px;
    font-family: "Questrial", "Century Gothic", sans-serif;
    font-size: 36px; line-height: 1; letter-spacing: 1px; color: var(--tag-green);
  }

  .details {
    position: absolute; left: 92px;
    font-family: "Gentium Book Plus", Georgia, serif;
    font-size: 26px; line-height: 1; color: var(--ink);
  }
  .audience { top: 515px; }
  .business { top: 589px; }
  .contact { top: 639px; }
  .phone { top: 683px; display: flex; align-items: center; gap: 14px; }
  .phone-icon { width: 36px; height: 36px; display: block; }
</style>
</head>
<body>
  <main class="card">
    <div class="scene-backdrop" role="img" aria-label="Faded grey photograph of a park with a leafless tree and a wire fence"></div>
    <div class="figure-art" role="img" aria-label="Line drawing of a tai chi practitioner in a stance with arms raised"></div>

    <h1 class="title">TAI CHI</h1>
    <p class="subtitle">FOR ALL</p>
    <p class="tagline">Be Healthy, Learn Tai Chi</p>

    <p class="details audience">All ages, gender or fitness levels</p>
    <p class="details business">Marrowdene Flowing Arts for Body, Mind &amp; Stillness</p>
    <p class="details contact">Contact Ms Brenna Holcroft:</p>
    <p class="details phone">
      <svg class="phone-icon" viewBox="0 0 36 36" aria-hidden="true">
        <rect width="36" height="36" rx="7" fill="#111"/>
        <path d="M12 8c1.5-.8 2.6-.4 3.2.9l1.6 3.4c.4.9.1 1.8-.7 2.3l-1.3.8c.8 2.6 2.3 5 4.2 6.8l1.3-.8c.8-.5 1.8-.4 2.4.4l2.3 2.9c.8 1.1.6 2.3-.7 3.1l-1.4.9c-1.6 1-4.2.3-6.6-1.9-3.2-3-5.6-7.3-6.3-11.1-.4-2.4.3-4.5 1.6-5.3z" fill="#fff"/>
      </svg>
      <span class="phone-number">5281 9046</span>
    </p>
  </main>
</body>
</html>
```